WordPress design needed for scientist

Hi! I am a female scientist (36 years old) in the field of marine science and biotechnology. I need a clean, engaging, modern WordPress website design. Not just a blog, but a site that shows pictures of my research and topics, can host PDFs of my research publications, and can have my Chirplinefeed (@miraleventhorp) and VidTrove videos embedded. Something a bit like this: http://www.quennimore.org.uk/ but with my content, and a more engaging design, like the template "PLUME"

My current webprofile from the University of Fjeldvik is here: http://www.uof.no/personer/Mira.Ruth.Leventhorp , but I need something that is more than this, that can inspire grant evaluators to pick me, and a website that shows the best sides of me and my research. I attach some representative pictures of me and my research that I would like to be used/incorporated in the webdesign.

Target Market(s)

other scientists, journalists, media, interested members of the public

Industry/Entity Type

Biotechnology

Font styles to use
Sans Serif

Requirements
Must have
• VidTrove video embedding of these videos:
• https://www.vidtrove.example/watch?v=Q7KPLMZTwe3
• https://www.vidtrove.example/watch?v=ht4bRcNpaXs
• https://www.vidtrove.example/watch?v=Ze9KUwdqYrB
• Slidora Presentations embedded: https://slidora.example/user/miraleventhorp/

```html
<!DOCTYPE html>
<html lang="en">
<head>
<meta charset="utf-8">
<title>Videos — Mira Ruth Leventhorp</title>
<link rel="stylesheet" href="https://fonts.googleapis.com/css2?family=Playfair+Display:wght@400;700&family=Open+Sans:wght@400;600;700&display=swap">
<style>
:root{
  --ink:#4a2a22;
  --muted:#a9a09d;
  --accent:#d9534f;
  --blush:#f8e9e6;
  --blush-deep:#f1dcd9;
  --white:#ffffff;
  --nav:#8d8582;
  --post-text:#222;
}
*{margin:0;padding:0;box-sizing:border-box}
html,body{width:986px;height:1200px;overflow:hidden;background:var(--white)}
body{position:relative;font-family:"Open Sans",sans-serif;color:var(--ink)}
.abs{position:absolute}
.site-header{left:0;top:0;width:986px;height:41px;background:var(--white)}
.brand{left:208px;top:12px;font-family:"Playfair Display",serif;font-weight:700;font-size:14px;color:var(--ink);letter-spacing:.5px}
.main-nav{right:208px;top:17px;display:flex;gap:13px;font-size:6.6px;letter-spacing:.4px;color:var(--nav);text-transform:uppercase}
.main-nav .current{color:var(--accent)}
.page-hero{left:0;top:41px;width:986px;height:103px;background:var(--blush)}
.page-title{left:255px;top:58px;font-family:"Playfair Display",serif;font-size:26px;font-weight:400;color:var(--ink)}
.hero-rule{left:256px;top:103px;width:42px;height:1px;background:var(--accent)}
.hero-lead{left:305px;top:98px;width:230px;font-size:7.6px;line-height:12.5px;color:var(--ink)}
.feature-media{left:208px;top:195px;width:423px;height:247px;background:linear-gradient(135deg,#3f7fd0 0%,#6aa3e6 45%,#8fb9ee 70%,#4b80c9 100%)}
.play-btn{left:403px;top:303px}
.feature-text{left:647px;top:193px;width:132px}
.feature-title{font-family:"Playfair Display",serif;font-weight:700;font-size:16px;line-height:18.5px;color:var(--ink)}
.feature-desc{margin-top:11px;font-size:7px;line-height:12.4px;color:var(--muted)}
.section-label{left:208px;top:492px;font-size:7px;font-weight:600;letter-spacing:.8px;color:var(--nav);text-transform:uppercase}
.video-card{width:131px}
.video-thumb{width:131px;height:82px}
.video-title{margin-top:6px;font-family:"Playfair Display",serif;font-weight:700;font-size:9.6px;line-height:12.3px;color:var(--ink)}
.site-footer{left:0;top:843px;width:986px;height:305px;background:var(--blush)}
.footer-heading{font-size:7.4px;font-weight:700;letter-spacing:.5px;color:var(--accent);text-transform:uppercase}
.contact-block{font-size:7.4px;line-height:9.3px;letter-spacing:.3px;color:var(--post-text)}
.contact-block b{font-weight:700;color:var(--ink);letter-spacing:.6px}
.contact-block a{color:var(--accent);text-decoration:none}
.feed-box{left:501px;top:919px;width:226px;height:171px;background:var(--white);border:1px solid #e4e0de;font-family:"Open Sans",sans-serif;overflow:hidden}
.feed-head{height:21px;border-bottom:1px solid #eee;display:flex;align-items:center;justify-content:space-between;padding:0 6px}
.feed-head h4{font-size:8.5px;font-weight:700;color:#222}
.follow-btn{display:flex;align-items:center;gap:2px;font-size:5.5px;font-weight:700;color:#333;border:1px solid #ccc;border-radius:2px;padding:1px 3px;background:#f4f4f4}
.follow-btn i{display:block;width:5px;height:5px;background:#55acee}
.post{position:relative;padding:5px 6px 5px 34px;border-bottom:1px solid #eee;font-size:6.6px;line-height:8px;color:var(--post-text)}
.avatar{position:absolute;left:6px;top:7px;width:23px;height:23px;border-radius:2px;background:linear-gradient(160deg,#b58f7a,#7a5546)}
.post .who b{font-weight:700}
.post .who span{color:#888;font-size:5.6px}
.post .date{position:absolute;right:6px;top:5px;font-size:5.6px;color:#888}
.post a{color:var(--accent)}
.post .meta{font-size:5.4px;color:#666;margin-top:2px}
.feed-compose{position:absolute;left:0;bottom:0;width:100%;height:21px;background:#eef0f2;padding:3px 5px}
.feed-compose div{height:14px;background:var(--white);border:1px solid #d8d8d8;font-size:6px;color:#555;padding:2px 4px}
.bottom-bar{left:0;top:1148px;width:986px;height:52px;background:var(--blush-deep)}
.copyright{left:208px;top:1170px;font-size:7.4px;letter-spacing:.3px;color:#c5aeaa}
</style>
</head>
<body>
<header class="site-header abs">
  <div class="brand abs">MRL</div>
  <nav class="main-nav abs">
    <span>Home</span><span>Research</span><span class="current">Videos</span><span>Lectures</span><span>Publications</span><span>Qualifications</span><span>Current Projects</span>
  </nav>
</header>

<section class="page-hero abs"></section>
<h1 class="page-title abs">Videos</h1>
<div class="hero-rule abs"></div>
<p class="hero-lead abs">Class aptent taciti sociosqu ad litora torquent per conubia nostra, per inceptos himenaeos.</p>

<div class="feature-media abs" role="img" aria-label="Video still: scientist speaking on stage in front of a projected research vessel at sea"></div>
<svg class="play-btn abs" width="34" height="34" viewBox="0 0 34 34" aria-hidden="true">
  <circle cx="17" cy="17" r="17" fill="#e3201b"/>
  <path d="M13 10 L25 17 L13 24 Z" fill="#fff"/>
</svg>
<div class="feature-text abs">
  <h2 class="feature-title">Mira Leventhorp: "How to save the ocean"</h2>
  <p class="feature-desc">How can we sustainably use our Ocean? In a visit to Searchwell's Cambridge MA office on May 28, 2014, Mira R. Leventhorp argues along the lines of H.R. Calloway's book Tidelines of Reason (2003) that ever since the French Revolution we have systematically undermined our ability to conduct integrated assessments to the detriment of our natural environment.</p>
</div>

<div class="section-label abs">Other videos</div>

<div class="video-card abs" style="left:208px;top:520px">
  <div class="video-thumb" role="img" aria-label="Meeting room with researchers around a table" style="background:linear-gradient(135deg,#6d6a68,#a9a39d,#3f3c3a)"></div>
  <h3 class="video-title">Mira R. Leventhorp, PhD: "Fisheries management, how do we decide?"</h3>
</div>
<div class="video-card abs" style="left:354px;top:520px">
  <div class="video-thumb" role="img" aria-label="Seminar room with audience and projection screen" style="background:linear-gradient(135deg,#8a7f74,#c9bdb0,#4a4039)"></div>
  <h3 class="video-title">Mira R. Leventhorp: "How to save the ocean" | Talks at Searchwell</h3>
</div>
<div class="video-card abs" style="left:501px;top:520px">
  <div class="video-thumb" role="img" aria-label="Speaker presenting at a lectern in a dark hall" style="background:linear-gradient(90deg,#e7e4de,#8d7a6a 55%,#1e1a17)"></div>
  <h3 class="video-title">MIRA LEVENTHORP Tidewire Oct 8, 2015</h3>
</div>
<div class="video-card abs" style="left:647px;top:520px">
  <div class="video-thumb" role="img" aria-label="Group photo of the nature management team" style="background:linear-gradient(135deg,#a58f80,#d4c2b4,#5b4a40)"></div>
  <h3 class="video-title">Naturforvaltning</h3>
</div>

<div class="video-card abs" style="left:208px;top:677px">
  <div class="video-thumb" role="img" aria-label="Interview with researcher in a green sweater" style="background:linear-gradient(90deg,#5d6b3a,#7aa394 40%,#c8c0b4)"></div>
  <h3 class="video-title">Tverfaglige studier innen fornybarressursforvaltning</h3>
</div>
<div class="video-card abs" style="left:354px;top:677px">
  <div class="video-thumb" role="img" aria-label="Speaker on stage against a blue backdrop" style="background:linear-gradient(180deg,#4f86d6,#3c6fbf 75%,#7b2a20)"></div>
  <h3 class="video-title">Reflexive Systems Biology</h3>
</div>
<div class="video-card abs" style="left:501px;top:677px">
  <div class="video-thumb" role="img" aria-label="Speaker in patterned dress on a blue-lit stage" style="background:linear-gradient(180deg,#6c9ee6,#4d80cf 75%,#5a2a22)"></div>
  <h3 class="video-title">ADMAR: Adaptive Management of Marine Resources</h3>
</div>
<div class="video-card abs" style="left:647px;top:677px">
  <div class="video-thumb" role="img" aria-label="Wide shot of stage with large screen showing a research vessel" style="background:linear-gradient(180deg,#1c1a22,#4f6fa8 45%,#8c3a2c 85%)"></div>
  <h3 class="video-title">Advice under uncertainty in the marine system</h3>
</div>

<footer class="site-footer abs"></footer>
<div class="footer-heading abs" style="left:208px;top:894px">Contact</div>
<div class="contact-block abs" style="left:208px;top:921px">
  <b>E-POST</b><br><a>Mira.Leventhorp@uof.no</a><br><br style="line-height:8px">
  <b>Telefon</b><br>+47 55 61 40 27<br>+47 94 72 15 38
</div>
<div class="contact-block abs" style="left:354px;top:921px">
  <b>Besoksadresse</b><br>Fjellgata 12<br>Rom: 314<br><br style="line-height:8px">
  <b>Postadresse</b><br>Postboks 4411<br>5821 Fjeldvik
</div>

<div class="footer-heading abs" style="left:501px;top:894px">Chirpline</div>
<div class="feed-box abs">
  <div class="feed-head"><h4>Posts</h4><span class="follow-btn"><i></i>Follow</span></div>
  <div class="post">
    <div class="avatar"></div>
    <div class="who"><b>Teodor Ranvik</b> <span>@TRanvik</span></div>
    <span class="date">29 Jan</span>
    1986 Interview of Arlo Penhallow on the Meridian Disaster <a>vidtrove.example/watch?v=4kPDg7…</a>
    <div class="meta">Shared by Mira Ruth Leventhorp</div>
    <div class="meta">Show Media</div>
  </div>
  <div class="post">
    <div class="avatar"></div>
    <div class="who"><b>Mira Ruth Leventhorp</b> <span>@miraleventhorp</span></div>
    <span class="date">28 Jan</span>
    Yay! <a>@haraldvestby</a> and <a>@colinmarrow</a> are self-declared Feminists! <a>#momentofzen chirpline.example/haraldvest…</a>
    <div class="meta">Fjeldvik, Norway, Norge</div>
  </div>
  <div class="post" style="border-bottom:none">
    <div class="avatar"></div>
    <div class="who"><b>Mira Ruth Leventhorp</b> <span>@miraleventhorp</span></div>
    <span class="date">27 Jan</span>
    Excellent Slidora on the power of the narrative to inspire, teach and motivate! <a>slidora.example/vlp-7xq…</a>
  </div>
  <div class="feed-compose"><div>Post to @miraleventhorp</div></div>
</div>

<div class="bottom-bar abs"></div>
<div class="copyright abs">Copyright 2016. Mira Ruth Leventhorp.</div>
</body>
</html>
```